Modern Label for cleaning products for the brand Voralux

We need a label design for our line of cleaning products. The label should feature our logo and an image to identify the product's intended use. I've added our logo and an image for use. This only concerns the design of the label on the front of the bottle.

Label dimensions:
Label 1 (500ml bottle with spray): width 58mm x height 115mm
Label 2: (1L bottle): width 73mm x height 140mm
The design must be consistent for both bottles which you find in the pictures.

The bottles to be labeled are white. See the attachment for a photo of the bottles.

The photo must also appear on the label to identify the product's intended use.

Product information:
Brand: Voralux
Product: Sanitary Cleaner

This text must be placed on the label:
"Cleans, descales & freshens. followed with this text: "Ideal for quick and powerful cleaning. A ready-to-use product for everyday use."

- Mention the seperate USP's: Sanitary, Bathroom, Toilet, Wet areas

Appearance: This is a consumer product, but it must have a professional appearance. We would like to see a design that use the color blue from our logo.

Target Market(s)

Consumers who take care of their homes and want to maintain it the correct (professional) way

Font styles to use
Sans Serif

Colors
0054AA
0677BA
7BADD7
CADEEF
E8F1F8

Requirements
Must have
• USP's + use of image and logo + blend in 1 design
Nice to have
• Keep the color of the logo in the design
Should not have
• Comic sans

```html
<!DOCTYPE html>
<html lang="en">
<head>
<meta charset="utf-8">
<title>Voralux Sanitary Cleaner – Front Labels</title>
<link rel="stylesheet" href="https://fonts.googleapis.com/css2?family=Barlow:wght@500;600;700&family=Barlow+Condensed:wght@600&display=swap">
<style>
  :root {
    --backdrop: #eeeeec;
    --blue-deep: #0a3596;
    --blue-bright: #0a8ff0;
    --blue-pill: #0a49b8;
    --blue-text: #0054aa;
    --mist: #dfe3e8;
    --white: #ffffff;
    --ink: #161616;
    --photo-top: #e6e8eb;
    --photo-mid: #b8b8ba;
    --photo-low: #8e8b89;
  }
  html, body {
    margin: 0;
    padding: 0;
    overflow: hidden;
  }
  body {
    width: 1200px;
    height: 1013px;
    background: var(--backdrop);
    position: relative;
  }
  .label {
    position: absolute;
    display: block;
    box-shadow: 0 2px 10px rgba(0,0,0,0.12);
  }
  .label--spray { left: 190px; top: 330px; width: 237px; height: 468px; }
  .label--litre { left: 700px; top: 203px; width: 317px; height: 607px; }
  .headline {
    font-family: "Barlow Condensed", "Arial Narrow", sans-serif;
    font-weight: 600;
    fill: var(--white);
  }
  .tagline {
    font-family: "Barlow", Arial, sans-serif;
    font-weight: 600;
    fill: var(--blue-text);
  }
  .pill { fill: var(--blue-pill); }
  .pill-text {
    font-family: "Barlow", Arial, sans-serif;
    font-weight: 600;
    fill: var(--white);
  }
  .pill-icon { fill: none; stroke: var(--white); stroke-width: 1.6; }
  .brand-mark { fill: none; stroke: var(--blue-text); }
  .brand-name {
    font-family: "Barlow", Arial, sans-serif;
    font-weight: 700;
    fill: var(--ink);
  }
</style>
</head>
<body>

<!-- 500 ml spray bottle label -->
<svg class="label label--spray" viewBox="0 0 412 815" xmlns="http://www.w3.org/2000/svg">
  <defs>
    <linearGradient id="bandSpray" x1="0" y1="0" x2="1" y2="0">
      <stop offset="0" stop-color="var(--blue-deep)"/>
      <stop offset="1" stop-color="var(--blue-bright)"/>
    </linearGradient>
    <linearGradient id="photoSpray" x1="0" y1="0" x2="0" y2="1">
      <stop offset="0" stop-color="var(--photo-top)"/>
      <stop offset="0.45" stop-color="var(--photo-mid)"/>
      <stop offset="1" stop-color="var(--photo-low)"/>
    </linearGradient>
  </defs>
  <rect class="label-base" width="412" height="815" fill="var(--white)"/>
  <polygon class="mist-band" points="0,238 412,145 412,330 0,330" fill="var(--mist)"/>
  <polygon class="bathroom-photo" role="img" aria-label="Modern bathroom with glass shower, washbasin cabinet and pebble-tiled bath"
           points="0,300 412,300 412,610 0,700" fill="url(#photoSpray)"/>
  <polygon class="title-band" points="0,0 412,0 412,145 0,238" fill="url(#bandSpray)"/>

  <g transform="rotate(-12.8 36 155)">
    <text class="headline" x="36" y="155" font-size="54" textLength="345" lengthAdjust="spacingAndGlyphs">CLEANS, DESCALES</text>
    <text class="headline" x="36" y="208" font-size="54" textLength="225" lengthAdjust="spacingAndGlyphs">&amp; FRESHENS</text>
  </g>
  <g transform="rotate(-12.8 36 257)">
    <text class="tagline" x="36" y="257" font-size="16" textLength="315" lengthAdjust="spacingAndGlyphs">Ideal for quick and powerful cleaning.</text>
    <text class="tagline" x="36" y="280" font-size="16" textLength="345" lengthAdjust="spacingAndGlyphs">A ready-to-use product for everyday use.</text>
  </g>

  <g class="usp-list">
    <rect class="pill" x="241" y="280" width="130" height="25" rx="12.5"/>
    <circle class="pill-icon" cx="258" cy="292.5" r="5"/>
    <text class="pill-text" x="275" y="298" font-size="16">Sanitary</text>
    <rect class="pill" x="241" y="310" width="130" height="25" rx="12.5"/>
    <circle class="pill-icon" cx="258" cy="322.5" r="5"/>
    <text class="pill-text" x="275" y="328" font-size="16">Bathroom</text>
    <rect class="pill" x="241" y="340" width="130" height="25" rx="12.5"/>
    <circle class="pill-icon" cx="258" cy="352.5" r="5"/>
    <text class="pill-text" x="275" y="358" font-size="16">Toilet</text>
    <rect class="pill" x="241" y="370" width="130" height="25" rx="12.5"/>
    <circle class="pill-icon" cx="258" cy="382.5" r="5"/>
    <text class="pill-text" x="275" y="388" font-size="16">Wet areas</text>
  </g>

  <circle class="brand-mark" cx="206" cy="718" r="36" stroke-width="7"/>
  <text class="brand-name" x="206" y="792" font-size="38" text-anchor="middle">Voralux</text>
</svg>

<!-- 1 L bottle label -->
<svg class="label label--litre" viewBox="0 0 552 1057" xmlns="http://www.w3.org/2000/svg">
  <defs>
    <linearGradient id="bandLitre" x1="0" y1="0" x2="1" y2="0">
      <stop offset="0" stop-color="var(--blue-deep)"/>
      <stop offset="1" stop-color="var(--blue-bright)"/>
    </linearGradient>
    <linearGradient id="photoLitre" x1="0" y1="0" x2="0" y2="1">
      <stop offset="0" stop-color="var(--photo-top)"/>
      <stop offset="0.45" stop-color="var(--photo-mid)"/>
      <stop offset="1" stop-color="var(--photo-low)"/>
    </linearGradient>
  </defs>
  <rect class="label-base" width="552" height="1057" fill="var(--white)"/>
  <polygon class="mist-band" points="0,313 552,187 552,420 0,420" fill="var(--mist)"/>
  <polygon class="bathroom-photo" role="img" aria-label="Modern bathroom with glass shower, washbasin cabinet and pebble-tiled bath"
           points="0,380 552,380 552,785 0,910" fill="url(#photoLitre)"/>
  <polygon class="title-band" points="0,0 552,0 552,187 0,313" fill="url(#bandLitre)"/>

  <g transform="rotate(-12.8 57 205)">
    <text class="headline" x="57" y="205" font-size="72" textLength="452" lengthAdjust="spacingAndGlyphs">CLEANS, DESCALES</text>
    <text class="headline" x="57" y="275" font-size="72" textLength="295" lengthAdjust="spacingAndGlyphs">&amp; FRESHENS</text>
  </g>
  <g transform="rotate(-12.8 57 338)">
    <text class="tagline" x="57" y="338" font-size="21" textLength="410" lengthAdjust="spacingAndGlyphs">Ideal for quick and powerful cleaning.</text>
    <text class="tagline" x="57" y="370" font-size="21" textLength="440" lengthAdjust="spacingAndGlyphs">A ready-to-use product for everyday use.</text>
  </g>

  <g class="usp-list">
    <rect class="pill" x="322" y="358" width="170" height="32" rx="16"/>
    <circle class="pill-icon" cx="345" cy="374" r="6"/>
    <text class="pill-text" x="368" y="382" font-size="22">Sanitary</text>
    <rect class="pill" x="322" y="397" width="170" height="32" rx="16"/>
    <circle class="pill-icon" cx="345" cy="413" r="6"/>
    <text class="pill-text" x="368" y="421" font-size="22">Bathroom</text>
    <rect class="pill" x="322" y="436" width="170" height="32" rx="16"/>
    <circle class="pill-icon" cx="345" cy="452" r="6"/>
    <text class="pill-text" x="368" y="460" font-size="22">Toilet</text>
    <rect class="pill" x="322" y="475" width="170" height="32" rx="16"/>
    <circle class="pill-icon" cx="345" cy="491" r="6"/>
    <text class="pill-text" x="368" y="499" font-size="22">Wet areas</text>
  </g>

  <circle class="brand-mark" cx="276" cy="930" r="47" stroke-width="9"/>
  <text class="brand-name" x="276" y="1025" font-size="50" text-anchor="middle">Voralux</text>
</svg>

</body>
</html>
```